Silver Ridge Business Card Design

I have an existing corporate logo. I'd like to clean it up bit (sharpen it up) and make it look better (without major redesign). I'd like to get the logo itself in all major file formats for print, web, etc.
Then I'd like a business card design that reflects a strategy consulting firm. It should be clean - logo and text without major graphics, and perhaps some small color treatments that match the logo color. The card should suggest high quality in terms of the company.
I'd like the files for card in all major print formats.
Target Market(s)
Silver Ridge Partners is a strategy development and business consulting firm focused on small to mid-sized companies. We specialize in business strategy, comprehensive business plan development, market segmentation and positioning, financial models, marketing and sales strategy, product strategy and the effective use of social media in business growth. We operate as consultants, advisers, retained members of management teams, and Board members. We often serve in the role of Chief Strategy Officer, supporting CEO's and other senior executives to enhance top and bottom line growth.
Our overall approach with clients is to deliver actual results, and we often take an active team role with business founders and management teams to drive business growth and affect real changes in performance. As a result, we approach each situation uniquely and partner with clients in a manner that will have the biggest impact on enterprise value.
Business
Look and feel

```html
<!DOCTYPE html>
<html lang="en">
<head>
<meta charset="utf-8">
<title>Silver Ridge Partners – Business Card</title>
<link rel="stylesheet" href="https://fonts.googleapis.com/css2?family=Arimo:wght@400;700&family=Open+Sans:wght@400;600;700&display=swap">
<style>
  :root {
    --bg: #e9e6e1;
    --card-white: #f7f7f7;
    --navy: #2f3f86;
    --navy-light: #4a5ba6;
    --navy-dark: #232f6a;
    --stripe: #1c1f2b;
    --ink: #1d1d1d;
    --text-light: #ffffff;
    --muted: #3a3a3a;
  }
  * { margin: 0; padding: 0; box-sizing: border-box; }
  html, body { width: 1200px; height: 885px; overflow: hidden; }
  body {
    background: var(--bg);
    position: relative;
    font-family: "Arimo", Arial, sans-serif;
  }
  .card {
    position: absolute;
    width: 600px;
    height: 343px;
    border-radius: 14px;
    overflow: hidden;
    box-shadow: 0 10px 26px rgba(0,0,0,0.22);
  }
  /* Front */
  .card-front { left: 60px; top: 80px; background: var(--card-white); }
  .front-top {
    height: 140px;
    display: flex;
    align-items: center;
    justify-content: space-between;
    padding: 0 44px 0 40px;
    background: linear-gradient(180deg, #ffffff, #ececec);
  }
  .brand { display: flex; align-items: center; gap: 14px; }
  .brand-dot { width: 34px; height: 34px; border-radius: 50%; background: var(--navy); }
  .brand-name {
    font-family: "Open Sans", Arial, sans-serif;
    font-weight: 700;
    font-size: 21px;
    line-height: 1.05;
    letter-spacing: 0.5px;
    text-transform: uppercase;
    color: var(--ink);
  }
  .person { text-align: right; }
  .person-name {
    font-family: "Open Sans", Arial, sans-serif;
    font-weight: 700;
    font-size: 24px;
    color: var(--navy);
    text-transform: uppercase;
    letter-spacing: 0.3px;
  }
  .person-title {
    font-family: "Open Sans", Arial, sans-serif;
    font-weight: 600;
    font-size: 13px;
    color: var(--muted);
    margin-top: 2px;
  }
  .front-stripe { height: 9px; background: var(--stripe); }
  .front-bottom {
    height: 194px;
    background: linear-gradient(160deg, var(--navy-light), var(--navy) 55%, var(--navy-dark));
    display: flex;
    align-items: center;
    padding: 0 40px;
    color: var(--text-light);
    font-size: 15px;
  }
  .contact-col { flex: 1; }
  .contact-divider { width: 1px; height: 80px; background: rgba(255,255,255,0.85); margin: 0 34px; }
  .contact-line { display: flex; align-items: center; gap: 10px; line-height: 25px; white-space: nowrap; }
  .icon { width: 13px; height: 13px; flex: none; fill: var(--text-light); }
  /* Back */
  .card-back {
    left: 540px; top: 462px;
    background: linear-gradient(160deg, var(--navy-light), var(--navy) 55%, var(--navy-dark));
    display: flex;
    align-items: center;
    justify-content: center;
  }
  .services {
    list-style: none;
    text-align: center;
    color: var(--text-light);
    font-size: 15.5px;
    line-height: 22px;
  }
</style>
</head>
<body>
  <section class="card card-front" aria-label="Business card front">
    <div class="front-top">
      <div class="brand">
        <span class="brand-dot"></span>
        <span class="brand-name">Silver Ridge<br>Partners, LLC</span>
      </div>
      <div class="person">
        <div class="person-name">Daniel K. Marsh</div>
        <div class="person-title">Partner and Founder</div>
      </div>
    </div>
    <div class="front-stripe"></div>
    <div class="front-bottom">
      <div class="contact-col">
        <div class="contact-line">
          <svg class="icon" viewBox="0 0 24 24"><path d="M6.6 10.8a15 15 0 0 0 6.6 6.6l2.2-2.2a1 1 0 0 1 1-.25 11.4 11.4 0 0 0 3.6.57 1 1 0 0 1 1 1V20a1 1 0 0 1-1 1A17 17 0 0 1 3 4a1 1 0 0 1 1-1h3.5a1 1 0 0 1 1 1c0 1.25.2 2.45.57 3.6a1 1 0 0 1-.25 1z"/></svg>
          <span>312.555.0148</span>
        </div>
        <div class="contact-line">
          <svg class="icon" viewBox="0 0 24 24"><path d="M2 5h20v14H2z M2 5l10 8 10-8" fill="none" stroke="#fff" stroke-width="2"/></svg>
          <span>dan@srpartners.com</span>
        </div>
        <div class="contact-line">
          <svg class="icon" viewBox="0 0 24 24"><circle cx="12" cy="12" r="9"/></svg>
          <span>srpartners.com/team/dkmarsh</span>
        </div>
        <div class="contact-line">
          <svg class="icon" viewBox="0 0 24 24"><circle cx="12" cy="12" r="9"/></svg>
          <span>@DanielMarsh</span>
        </div>
      </div>
      <div class="contact-divider"></div>
      <div class="contact-col">
        <div class="contact-line">
          <svg class="icon" viewBox="0 0 24 24"><path d="M12 2a7 7 0 0 0-7 7c0 5 7 13 7 13s7-8 7-13a7 7 0 0 0-7-7zm0 9.5A2.5 2.5 0 1 1 12 6.5a2.5 2.5 0 0 1 0 5z"/></svg>
          <span>412 Alder Crest Lane</span>
        </div>
        <div class="contact-line">
          <span class="icon"></span>
          <span>Westfield, Illinois 60499</span>
        </div>
        <div class="contact-line">
          <svg class="icon" viewBox="0 0 24 24"><circle cx="12" cy="12" r="9" fill="none" stroke="#fff" stroke-width="2"/><path d="M3 12h18M12 3c3 3 3 15 0 18M12 3c-3 3-3 15 0 18" fill="none" stroke="#fff" stroke-width="1.6"/></svg>
          <span>srpartners.com</span>
        </div>
      </div>
    </div>
  </section>

  <section class="card card-back" aria-label="Business card back">
    <ul class="services">
      <li>Business strategy development and planning</li>
      <li>Identification of new market opportunities</li>
      <li>Go-to-market strategy</li>
      <li>Marketing and sales strategy</li>
      <li>New business development</li>
      <li>Comprehensive business plan development</li>
      <li>Strategic market positioning</li>
      <li>Operational turnarounds, improvement and stabilization</li>
      <li>Financial justification of strategic investments</li>
      <li>Strategic application of technology</li>
      <li>Portfolio analysis - profitability and prioritization</li>
      <li>Customer insights analysis</li>
    </ul>
  </section>
</body>
</html>
```